Income Tax and Accounting Brochure

I need a brochure using my new logo (file attached). I do tax work and accounting work. I am an EA (QVX Enrolled Agent - logo attached) and would like this incorporated into the brochure. I also have a MSA in Accounting. Please incorporate the text that I have provided in the brochure.
Updates

Need extra days to review

Target Market(s)

Tax Clients - both business and individuals

Industry/Entity Type

Accounting

Colors
0054AA
0677BA
7BADD7
CADEEF
E8F1F8

Requirements
Must have
• Use my logo and the QVX EA file in the brochure
Nice to have
• I would like to see a brochure that I can customize with my own text if possible.

```html
<!DOCTYPE html>
<html lang="en">
<head>
<meta charset="utf-8">
<title>MDH Accounting &amp; Consulting – Brochure</title>
<link href="https://fonts.googleapis.com/css2?family=Quicksand:wght@400;500;700&family=Rajdhani:wght@500;600&display=swap" rel="stylesheet">
<style>
:root{
  --backdrop:#5b5b5b;
  --paper:#ffffff;
  --brand-blue:#0054aa;
  --sky:#7fbff9;
  --ink-dark:#15181f;
  --ink:#1b1f27;
  --icon:#8ec9ff;
  --badge:#e4e6e2;
  --badge-edge:#a7a69a;
  --wordmark:#2f74c8;
}
*{margin:0;padding:0;box-sizing:border-box}
html,body{width:944px;height:1200px;overflow:hidden;background:var(--backdrop)}
.canvas{position:relative;width:944px;height:1200px}
.page{position:absolute;left:55px;top:60px;width:835px;height:1080px;background:var(--paper);overflow:hidden;font-family:"Quicksand",sans-serif}
.credential-badge{position:absolute;left:42px;top:26px;width:290px;height:72px;background:var(--badge);border:3px solid var(--badge-edge)}
.header-rule{position:absolute;left:0;top:111px;width:835px;height:9px;background:var(--brand-blue)}
.hero{position:absolute;left:0;top:120px;width:835px;height:400px;
  background:linear-gradient(90deg,#15181f 0%,#181b22 30%,#4c3a32 52%,#8a5a3e 72%,#9a6242 100%)}
.name-card{position:absolute;left:617px;top:74px;width:218px;height:83px;background:var(--brand-blue);color:#fff;padding:12px 0 0 23px}
.name-card h1{font-weight:400;font-size:26px;line-height:1.1}
.name-card p{font-weight:400;font-size:16px;margin-top:4px}
.copy{font-size:12.2px;line-height:16.6px;text-align:justify;font-weight:500;letter-spacing:-0.25px}
.about{position:absolute;left:38px;top:170px;width:300px;color:#fff}
.about h2{font-weight:400;font-size:25px;line-height:30px;margin-bottom:14px}
.about p + p{margin-top:16.6px}
.tax-panel{position:absolute;left:0;top:508px;width:512px;height:572px;background:var(--brand-blue);border-radius:0 22px 22px 0;color:#fff}
.tax-panel h2{position:absolute;left:35px;top:14px;font-weight:400;font-size:21px;line-height:28px;white-space:nowrap}
.tax-panel h2 b{font-weight:700}
.tax-panel .lead{position:absolute;left:35px;width:453px;text-indent:49px}
.tax-panel h3{position:absolute;left:35px;top:237px;font-weight:400;font-size:20.5px;line-height:26px;white-space:nowrap}
.benefit{position:absolute;left:35px;width:453px;display:flex;gap:11px;color:#fff}
.benefit svg{flex:0 0 55px}
.benefit p{width:387px}
.side-panel{position:absolute;left:516px;top:512px;width:319px;height:369px;background:var(--sky);border-radius:22px 0 0 0;color:var(--ink);padding:0 18px}
.side-panel p{font-family:"Rajdhani",sans-serif;font-weight:500;font-size:14.6px;line-height:18.5px}
.side-panel .indent{text-indent:49px}
.side-panel .first{margin-top:53px}
.side-panel h2{font-weight:400;font-size:19.5px;line-height:26px;margin:26px 0 14px;white-space:nowrap}
.side-panel h2 b{font-weight:700}
.brand-band{position:absolute;left:516px;top:881px;width:319px;height:121px;background:var(--ink-dark);display:flex;align-items:center;padding-left:38px;gap:10px}
.brand-band .mark{width:58px;height:58px;border-radius:50%;background:var(--wordmark);flex:none}
.brand-band .wordmark{font-family:"Quicksand",sans-serif;font-weight:500;color:var(--wordmark);font-size:16px;line-height:20px;letter-spacing:1.5px}
.contact{position:absolute;left:516px;top:1002px;width:319px;height:78px;background:var(--sky);border-radius:0 0 0 22px;padding:10px 0 0 42px}
.contact li{list-style:none;display:flex;align-items:center;gap:9px;font-family:"Rajdhani",sans-serif;font-weight:600;font-size:20px;color:var(--ink);height:28px}
</style>
</head>
<body>
<div class="canvas">
  <div class="page">
    <div class="credential-badge" aria-label="Enrolled agent credential badge"></div>
    <div class="header-rule"></div>
    <div class="hero" role="img" aria-label="Portrait of the principal in a dark suit leaning against a warm wooden slat wall"></div>
    <div class="name-card">
      <h1>Maren D Hollis</h1>
      <p>MSA EA (Principal)</p>
    </div>
    <section class="about">
      <h2>ABOUT US</h2>
      <p class="copy">I have a Masters' Degree in accounting and am an QVX Enrolled Agent. I am also a LedgerPro Advanced Certified Consultant in both the online and desktop products including Enterprise and Point of Sale. I provide individual and small business tax services, Accounting, bookkeeping, QVX representation, insurance audit representation, business license assistance and more.</p>
      <p class="copy">I have experience working with a wide variety of clients from the point where they first decide they want to start a business. They are often unsure about what to do first- I have a lot of experience to offer you. What a joy it is to watch success in action!</p>
    </section>

    <section class="tax-panel">
      <h2>TAX PREPARATION – <b>why hire us?</b></h2>
      <p class="copy lead" style="top:56px">Preparing your own income tax return can be a task that leaves you with more questions than answers. According to a study released by the US Government's Federal Audit Bureau last year, most taxpayers (77% of 71 million taxpayers) believe they benefited from using a professional tax preparer.</p>
      <p class="copy lead" style="top:139px">Whether we like it or not, today's tax laws are so complicated that filing a relatively simple return can be confusing. It is just too easy to overlook deductions and credits to which you are entitled. Even if you use a computer software program there's no substitute for the assistance of an experienced tax professional.</p>
      <h3>HERE'S WHAT YOUR GET...</h3>
    </section>

    <div class="benefit" style="top:780px">
      <svg width="55" height="46" viewBox="0 0 56 46" fill="none" stroke="var(--icon)" stroke-width="3"><rect x="8" y="3" width="40" height="30" rx="3"/><path d="M2 38h52l-3 5H5z" fill="var(--icon)"/><path d="M22 13l-5 5 5 5M34 13l5 5-5 5"/></svg>
      <p class="copy">Your tax return will be checked and rechecked by our computer software identifying potential problems the QVX may look at more closely and reviewing the math to limit QVX contacts.</p>
    </div>
    <div class="benefit" style="top:851px;align-items:center">
      <svg width="55" height="56" viewBox="0 0 56 56" fill="none" stroke="var(--icon)" stroke-width="2.5"><rect x="10" y="3" width="40" height="30" rx="2"/><circle cx="30" cy="18" r="8"/><path d="M26 22l8-8"/><path d="M2 44l12-8h14l8 4-10 2M2 53h18l22-10"/></svg>
      <p class="copy">Your tax return can be filed electronically so you will get a refund back quicker.</p>
    </div>
    <div class="benefit" style="top:930px">
      <svg width="55" height="58" viewBox="0 0 56 58" fill="none" stroke="var(--icon)" stroke-width="3"><path d="M4 3h28l10 10v30H4z"/><path d="M12 22h22M12 29h22M12 36h16"/><circle cx="46" cy="47" r="9" fill="var(--icon)"/><text x="46" y="52" font-size="13" font-family="Quicksand,sans-serif" font-weight="700" fill="var(--brand-blue)" stroke="none" text-anchor="middle">$</text></svg>
      <p class="copy">Our staff will show you how to adjust your payroll withholding to get more money back each week. Why give the QVX an interest free loan for up to 16 months.</p>
    </div>
    <div class="benefit" style="top:1010px">
      <svg width="55" height="52" viewBox="0 0 56 52" fill="none" stroke="var(--icon)" stroke-width="3"><rect x="4" y="3" width="38" height="16" rx="2"/><circle cx="23" cy="11" r="4"/><path d="M14 22l12 16M30 22l-12 16"/><circle cx="10" cy="44" r="5"/><circle cx="26" cy="44" r="5"/><path d="M38 28h14M38 34h14M38 40h14M38 46h14"/></svg>
      <p class="copy">We will show you potential deductions to limit your tax liability for next year. In addition, we will give you a sheet of commonly overlooked deductions to limit the following year's tax liability.</p>
    </div>

    <section class="side-panel">
      <p class="indent first">We will show you potential deductions to limit your tax liability for next year. In addition, we will give you a sheet of commonly overlooked deductions to limit the following year's tax liability.</p>
      <h2>BOOKS A MESS: <b>no problem!</b></h2>
      <p class="indent">If you own a small business and haven't kept up your bookkeeping, don't worry. We can help you. We'll prepare your bookkeeping for the year, prepare a full Schedule C, as well as your personal income tax return. Then we'll help you set up an easy system that allows you to keep your books in tip-top shape next year.</p>
    </section>

    <div class="brand-band">
      <span class="mark"></span>
      <span class="wordmark">MDH ACCOUNTING<br>&amp; CONSULTING, LLC</span>
    </div>

    <ul class="contact">
      <li><svg width="20" height="20" viewBox="0 0 20 20"><circle cx="10" cy="10" r="10" fill="var(--brand-blue)"/><path d="M6 11a4 4 0 0 1 8 0M5.5 10.5v3h2v-3zM12.5 10.5v3h2v-3z" fill="#fff" stroke="#fff" stroke-width="1"/></svg>000-000-0000</li>
      <li><svg width="20" height="20" viewBox="0 0 20 20"><circle cx="10" cy="10" r="10" fill="var(--brand-blue)"/><path d="M5 10l10-5-3 11-3-4z" fill="#fff"/></svg>info@MDHConsulting.com</li>
    </ul>
  </div>
</div>
</body>
</html>
```